A Flyer for a clinic/hospital waiting room to warn about patients that they must not abuse our staff

we need a flyer (text attached) with a background of a female nurse or medical doctor photo. I like the example photo where there are four headless satff lined up - something like this, indicating that we are a team and will not tolerate abuse
A4
the text will be over the photo.

Target Market(s)

patients who come to our clinic

Industry/Entity Type

medicine - urology

Colors
0054AA
0677BA
7BADD7
CADEEF
E8F1F8
0094D4
00A9DD
6FCCEA
C7EBF8
E9F6FB

Requirements
Must have
• a photo taking up the whole A4, and text over this. The photos I haev sent are just examples - I will need yo to source a photo
Nice to have
• Horizontal A4 and vertical A4 options. Please add our logo in small , in the bottom right corner

```html
<!DOCTYPE html>
<html lang="en">
<head>
<meta charset="utf-8">
<title>Zero Tolerance Flyer – RiverBend Urology</title>
<link rel="stylesheet" href="https://fonts.googleapis.com/css2?family=Oswald:wght@600;700&family=Roboto:wght@400;500;700&display=swap">
<style>
  :root {
    --navy: #243f8f;
    --blue-deep: #0054aa;
    --blue-mid: #0677ba;
    --blue-bright: #0094d4;
    --cyan: #00a9dd;
    --sky: #7badd7;
    --mist: #cadeef;
    --ice: #e8f1f8;
    --red: #e3232b;
    --yellow: #ffe33b;
    --white: #ffffff;
    --ink: #111111;
  }
  * { box-sizing: border-box; margin: 0; padding: 0; }
  html, body { width: 848px; height: 1200px; overflow: hidden; background: var(--white); }
  .flyer {
    position: relative;
    width: 848px;
    height: 1200px;
    overflow: hidden;
    font-family: "Roboto", Arial, sans-serif;
    color: var(--white);
  }
  .hero-photo {
    position: absolute;
    inset: 0 0 auto 0;
    height: 600px;
    background:
      linear-gradient(90deg, rgba(255,255,255,0.95) 0%, rgba(232,241,248,0.7) 45%, rgba(202,222,239,0) 60%),
      linear-gradient(160deg, var(--ice) 0%, var(--mist) 45%, #1e9bb5 70%, #2a8fa8 100%);
  }
  .waves { position: absolute; inset: 0; width: 848px; height: 1200px; }
  .headline {
    position: absolute;
    left: 50px;
    top: 62px;
    width: 390px;
    text-align: center;
  }
  .headline .lead {
    display: block;
    font-weight: 500;
    font-size: 27px;
    color: var(--ink);
    line-height: 1.1;
  }
  .headline .alarm {
    display: block;
    font-family: "Oswald", "Arial Narrow", sans-serif;
    font-weight: 700;
    font-size: 74px;
    line-height: 0.98;
    color: var(--red);
    letter-spacing: -0.5px;
    margin-top: 2px;
  }
  .headline .link {
    display: block;
    font-weight: 500;
    font-size: 25px;
    color: var(--ink);
    margin-top: 4px;
  }
  .headline .subject {
    display: block;
    font-family: "Oswald", "Arial Narrow", sans-serif;
    font-weight: 700;
    font-size: 76px;
    line-height: 1.02;
    color: var(--blue-deep);
    margin-top: 2px;
  }
  .tagline {
    position: absolute;
    top: 518px;
    left: 200px;
    width: 450px;
    text-align: center;
    font-weight: 700;
    font-size: 23px;
    line-height: 1.38;
  }
  .definition {
    position: absolute;
    left: 56px;
    top: 663px;
    width: 370px;
  }
  .definition h2 {
    font-size: 20px;
    font-weight: 700;
    color: var(--yellow);
    line-height: 1.28;
    margin-bottom: 8px;
  }
  .definition ul { list-style: none; }
  .definition li {
    position: relative;
    padding-left: 16px;
    font-size: 22px;
    line-height: 1.25;
    margin-bottom: 9px;
  }
  .definition li::before {
    content: "";
    position: absolute;
    left: 2px;
    top: 10px;
    width: 6px;
    height: 6px;
    border-radius: 50%;
    background: var(--yellow);
  }
  .policy {
    position: absolute;
    left: 471px;
    top: 660px;
    width: 330px;
    font-size: 15.5px;
    line-height: 1.3;
  }
  .policy p { margin-bottom: 15px; }
  .brand-badge {
    position: absolute;
    left: 602px;
    top: 982px;
    width: 170px;
    height: 170px;
    border-radius: 50%;
    background: var(--white);
    display: flex;
    align-items: center;
    justify-content: center;
    text-align: center;
  }
  .brand-badge .brand-name {
    font-family: "Roboto", Arial, sans-serif;
    font-weight: 500;
    font-size: 17px;
    line-height: 1.2;
    color: var(--blue-deep);
  }
</style>
</head>
<body>
<main class="flyer">
  <div class="hero-photo" role="img" aria-label="Photo of a nurse in teal scrubs with a stethoscope, arms crossed, head out of frame, in a bright clinic"></div>

  <svg class="waves" viewBox="0 0 848 1200" aria-hidden="true">
    <defs>
      <linearGradient id="panel" x1="0" y1="0" x2="0" y2="1">
        <stop offset="0" stop-color="#0a5ea8"/>
        <stop offset="0.35" stop-color="#0a7fc4"/>
        <stop offset="1" stop-color="#0c8fd0"/>
      </linearGradient>
    </defs>
    <path d="M0 515 C 160 460, 330 455, 480 470 C 640 485, 760 520, 848 560 L848 1200 L0 1200 Z" fill="var(--sky)"/>
    <path d="M0 545 C 170 480, 340 478, 500 492 C 650 506, 770 540, 848 575 L848 1200 L0 1200 Z" fill="url(#panel)"/>
    <path d="M0 580 C 220 620, 500 620, 848 560 L848 1200 L0 1200 Z" fill="var(--blue-bright)" opacity="0.35"/>
    <path d="M0 1090 C 240 1125, 520 1145, 848 1110 L848 1200 L0 1200 Z" fill="var(--sky)"/>
    <path d="M0 1112 C 260 1148, 540 1165, 848 1130 L848 1200 L0 1200 Z" fill="var(--navy)"/>
  </svg>

  <header class="headline">
    <span class="lead">We have</span>
    <span class="alarm">ZERO-<br>TOLERANCE</span>
    <span class="link">for any form of</span>
    <span class="subject">AGGRESSIVE<br>BEHAVIOUR</span>
  </header>

  <p class="tagline">Our staff treat you with respect and we expect the same in return</p>

  <section class="definition">
    <h2>Aggressive behaviour (in-<br>person or on the telephone) is:</h2>
    <ul>
      <li>Verbal harassment</li>
      <li>Any verbal or physical confrontation</li>
      <li>Raising your voice or making unreasonable demands</li>
      <li>Abusive or intimidating behaviour</li>
      <li>Sexual or suggestive language or behaviour</li>
      <li>Making threats to our staff</li>
      <li>Swearing</li>
    </ul>
  </section>

  <section class="policy">
    <p>If any of our staff feel intimidated in any way, we will always support them. Incidents will result in your immediate removal from the facility, termination of your relationship with the practice, and may result in prosecution.</p>
    <p>In all circumstances we will support any staff member who wishes to press charges against a perpetrator of aggressive behaviour.</p>
    <p>We take this stance because our staff work extremely hard in busy circumstances to help you and we will no longer tolerate any form of aggression or abuse.</p>
  </section>

  <div class="brand-badge">
    <span class="brand-name">RiverBend<br>Urology</span>
  </div>
</main>
</body>
</html>
```